Healthcare Consulting company business card

We are looking for a business card design for a new healthcare consulting company. The company is looking to provide assistance to large healthcare organisations in the following categories:
Acute care and critical care
Tender documents and applications
CV, job applications and interview skills
scientific lecture presentation preparations and skills
research and quality activities
medical equipment and device consulting
hemofiltration liaising.
Please see the attached file below for the design brief.
Alternative designs are welcomed.
Industry/Entity Type
Business
Contact Information for Business Card
Name: Rob Kettering
Mobile: 0427 861 093
Email: robketteringconsulting@mailvale.com
Website: www.robketteringconsulting.com.au

```html
<!DOCTYPE html>
<html lang="en">
<head>
<meta charset="utf-8">
<title>Rob Kettering Consulting – Business Card</title>
<link href="https://fonts.googleapis.com/css2?family=Arimo:wght@400;700&display=swap" rel="stylesheet">
<style>
  :root {
    --brand-blue: #245c9e;
    --tile-dark: #2b2b2d;
    --icon-light: #ffffff;
    --paper: #ffffff;
    --frame: #222222;
  }
  * { margin: 0; padding: 0; box-sizing: border-box; }
  html, body { width: 1200px; height: 1200px; overflow: hidden; background: var(--paper); }
  body { position: relative; font-family: "Arimo", Arial, sans-serif; color: var(--brand-blue); }

  .icon-defs { position: absolute; width: 0; height: 0; overflow: hidden; }

  .card { position: absolute; left: 180px; width: 838px; height: 478px; }
  .card--front { top: 94px; background: var(--paper); border: 1.5px solid var(--frame); }
  .card--back { top: 626px; background: var(--brand-blue); }

  .holder { position: absolute; left: 61px; top: 88px; }
  .holder__name { font-size: 35px; font-weight: 700; line-height: 1; }
  .holder__role { font-size: 26px; font-weight: 400; line-height: 1; margin-top: 6px; }

  .contact { position: absolute; left: 56px; top: 190px; list-style: none; }
  .contact__item { display: flex; align-items: center; height: 39px; font-size: 25px; }
  .contact__icon { width: 22px; height: 22px; margin-right: 20px; flex: none; }

  .wordmark { position: absolute; display: flex; align-items: center; font-weight: 400; line-height: 1.15; }
  .wordmark__dot { flex: none; border-radius: 50%; background: currentColor; }
  .card--front .wordmark { left: 555px; top: 84px; font-size: 25px; }
  .card--front .wordmark__dot { width: 22px; height: 22px; margin-right: 14px; }
  .card--back .wordmark { left: 0; right: 0; top: 142px; justify-content: center; font-size: 40px; color: var(--paper); }
  .card--back .wordmark__dot { width: 34px; height: 34px; margin-right: 20px; }
  .wordmark__text span { display: block; }

  .services { position: absolute; left: 57px; display: flex; gap: 69px; }
  .card--front .services { top: 351px; }
  .card--back .services { top: 339px; }
  .service-tile { width: 90px; height: 90px; border-radius: 5px; background: var(--tile-dark); display: block; }
</style>
</head>
<body>

<svg class="icon-defs" aria-hidden="true">
  <defs>
    <symbol id="icon-tender" viewBox="0 0 90 90">
      <rect width="90" height="90" rx="5" fill="#2b2b2d"/>
      <rect x="14" y="12" width="62" height="38" fill="none" stroke="#fff" stroke-width="3"/>
      <path d="M22 40 H68 M22 31 H54 M22 22 H60" stroke="#fff" stroke-width="3"/>
      <circle cx="30" cy="66" r="13" fill="none" stroke="#fff" stroke-width="3"/>
      <text x="30" y="73" text-anchor="middle" font-family="Arimo, Arial, sans-serif" font-size="19" font-weight="700" fill="#fff">$</text>
      <rect x="52" y="58" width="24" height="18" fill="none" stroke="#fff" stroke-width="3"/>
    </symbol>
    <symbol id="icon-heart" viewBox="0 0 90 90">
      <rect width="90" height="90" rx="5" fill="#2b2b2d"/>
      <path d="M45 76 C20 58 9 46 9 33 C9 21 18 13 28 13 C36 13 42 18 45 24 C48 18 54 13 62 13 C72 13 81 21 81 33 C81 46 70 58 45 76Z" fill="#fff"/>
      <polyline points="13,41 27,41 31,33 35,49 40,25 45,56 49,35 53,41 77,41" fill="none" stroke="#2b2b2d" stroke-width="2.2"/>
    </symbol>
    <symbol id="icon-bed" viewBox="0 0 90 90">
      <rect width="90" height="90" rx="5" fill="#2b2b2d"/>
      <rect x="9" y="42" width="6" height="36" fill="#fff"/>
      <rect x="75" y="52" width="6" height="26" fill="#fff"/>
      <rect x="15" y="58" width="60" height="8" fill="#fff"/>
      <circle cx="23" cy="51" r="5" fill="#fff"/>
      <rect x="30" y="50" width="42" height="6" fill="#fff"/>
      <path d="M37 10 V54" stroke="#fff" stroke-width="3"/>
      <rect x="46" y="14" width="30" height="22" fill="none" stroke="#fff" stroke-width="3"/>
      <polyline points="50,26 56,26 58,20 61,31 64,24 72,24" fill="none" stroke="#fff" stroke-width="1.8"/>
    </symbol>
    <symbol id="icon-lecture" viewBox="0 0 90 90">
      <rect width="90" height="90" rx="5" fill="#2b2b2d"/>
      <path d="M14 46 A31 31 0 0 1 76 46" fill="none" stroke="#fff" stroke-width="5" stroke-dasharray="2 3"/>
      <path d="M32 44 H58 L54 52 H36 Z" fill="#fff"/>
      <rect x="42" y="52" width="6" height="22" fill="#fff"/>
      <rect x="32" y="74" width="26" height="5" fill="#fff"/>
    </symbol>
    <symbol id="icon-research" viewBox="0 0 90 90">
      <rect width="90" height="90" rx="5" fill="#2b2b2d"/>
      <g fill="none" stroke="#fff" stroke-width="3">
        <path d="M14 34 V64 H24 V34 M24 40 V64 H34 V40"/>
        <path d="M12 50 H36"/>
      </g>
      <path d="M56 18 H66 M58 18 V38 L46 62 H78 L66 38 V18" fill="none" stroke="#fff" stroke-width="3" stroke-linejoin="round"/>
      <path d="M51 52 H73 L78 62 H46 Z" fill="#fff"/>
      <rect x="42" y="68" width="40" height="5" fill="#fff"/>
    </symbol>
  </defs>
</svg>

<section class="card card--front">
  <div class="holder">
    <h1 class="holder__name">Rob Kettering</h1>
    <p class="holder__role">Consulting</p>
  </div>

  <ul class="contact">
    <li class="contact__item">
      <svg class="contact__icon" viewBox="0 0 22 22" aria-hidden="true">
        <rect x="5" y="1" width="12" height="20" rx="2.5" fill="none" stroke="#245c9e" stroke-width="2.2"/>
        <circle cx="11" cy="17" r="1.4" fill="#245c9e"/>
      </svg>
      0427 861 093
    </li>
    <li class="contact__item">
      <svg class="contact__icon" viewBox="0 0 22 22" aria-hidden="true">
        <rect x="1" y="5" width="20" height="13" fill="#245c9e"/>
        <path d="M1 5 L11 13 L21 5 M1 18 L8.5 11 M21 18 L13.5 11" fill="none" stroke="#fff" stroke-width="1.3"/>
      </svg>
      robketteringconsulting@mailvale.com
    </li>
    <li class="contact__item">
      <svg class="contact__icon" viewBox="0 0 22 22" aria-hidden="true">
        <g fill="none" stroke="#245c9e" stroke-width="1.8">
          <circle cx="11" cy="11" r="9"/>
          <ellipse cx="11" cy="11" rx="4" ry="9"/>
          <path d="M2 11 H20 M3.5 6.5 H18.5 M3.5 15.5 H18.5"/>
        </g>
      </svg>
      www.robketteringconsulting.com.au
    </li>
  </ul>

  <div class="wordmark">
    <span class="wordmark__dot"></span>
    <span class="wordmark__text"><span>Rob Kettering</span><span>Consulting</span></span>
  </div>

  <div class="services">
    <svg class="service-tile" role="img" aria-label="Tenders and applications"><use href="#icon-tender"/></svg>
    <svg class="service-tile" role="img" aria-label="Acute and critical care"><use href="#icon-heart"/></svg>
    <svg class="service-tile" role="img" aria-label="Medical equipment and devices"><use href="#icon-bed"/></svg>
    <svg class="service-tile" role="img" aria-label="Lectures and presentations"><use href="#icon-lecture"/></svg>
    <svg class="service-tile" role="img" aria-label="Research and quality"><use href="#icon-research"/></svg>
  </div>
</section>

<section class="card card--back">
  <div class="wordmark">
    <span class="wordmark__dot"></span>
    <span class="wordmark__text"><span>Rob Kettering</span><span>Consulting</span></span>
  </div>

  <div class="services">
    <svg class="service-tile" role="img" aria-label="Tenders and applications"><use href="#icon-tender"/></svg>
    <svg class="service-tile" role="img" aria-label="Acute and critical care"><use href="#icon-heart"/></svg>
    <svg class="service-tile" role="img" aria-label="Medical equipment and devices"><use href="#icon-bed"/></svg>
    <svg class="service-tile" role="img" aria-label="Lectures and presentations"><use href="#icon-lecture"/></svg>
    <svg class="service-tile" role="img" aria-label="Research and quality"><use href="#icon-research"/></svg>
  </div>
</section>

</body>
</html>
```